New website for tarnova.se using wordpress

- Tarnova is a consultant broker based in Sweden
- Current web page: tarnova.se
- We want a new web page and we are aiming for simple and "clean"
- Two target groups:
1. Consultants/Consultant firms looking for assignments
2. Clients looking for consultants
- Colors + Logo attached

Requirements
Must have
• The new site should have separate pages the different sections. We have to be able to link to each page separately. NOT like the current web page where all the content is on one page.

```html
<!DOCTYPE html>
<html lang="en">
<head>
<meta charset="utf-8">
<title>Tarnova – Independent Consultants</title>
<link href="https://fonts.googleapis.com/css2?family=DM+Serif+Display&family=Poppins:wght@400;500;600&display=swap" rel="stylesheet">
<style>
:root{
  --purple:#6a319e;
  --purple-dark:#55237f;
  --ink:#1d1d22;
  --slate:#343a46;
  --footer:#2a2a2c;
  --muted:#5b5b66;
  --white:#ffffff;
  --line:#cfcfd6;
}
*{box-sizing:border-box;margin:0;padding:0}
html,body{width:1200px;height:5252px;overflow:hidden}
body{position:relative;font-family:'Poppins',sans-serif;color:var(--ink);background:var(--white)}
.abs{position:absolute}
.serif{font-family:'DM Serif Display',serif;font-weight:400}
.backdrop{position:absolute;left:0;top:0}
.photo{position:absolute}

.logo{font-family:'Poppins',sans-serif;font-weight:500;color:var(--white);letter-spacing:3px}
.nav{position:absolute;top:28px;left:562px;display:flex;gap:18px;font-size:13px;font-weight:500;color:var(--white);text-transform:uppercase}
.hero-kicker{left:173px;top:468px;font-size:46px;color:var(--white)}
.hero-title{left:168px;top:530px;font-size:142px;line-height:1;color:var(--white)}

.kicker{font-size:30px}
.heading{font-size:44px;text-transform:uppercase;line-height:1.1}
.on-purple{color:var(--white)}
.body-text{font-size:11.5px;line-height:24px}

.blob{position:absolute;border-radius:48% 52% 40% 60% / 55% 45% 55% 45%}
.dot{position:absolute;border-radius:50%;background:var(--slate)}

.bullets{list-style:none;width:446px}
.bullets li{position:relative;padding-left:18px;font-size:11.5px;line-height:21px;margin-bottom:14px;color:var(--ink)}
.bullets li::before{content:"";position:absolute;left:0;top:5px;border-left:9px solid var(--purple);border-top:6px solid transparent;border-bottom:6px solid transparent}

.pill{position:absolute;top:1994px;height:68px;width:266px;border-radius:14px;background:var(--white);display:flex;align-items:center;justify-content:center;font-weight:600;font-size:17px;letter-spacing:.5px;color:var(--ink);box-shadow:0 6px 14px rgba(0,0,0,.18)}
.pill.active{background:var(--purple);border:3px solid var(--white);color:var(--white)}
.node{position:absolute;top:2181px;width:160px;height:160px;border-radius:50%;background:var(--white);display:flex;flex-direction:column;align-items:center;justify-content:center;text-align:center;font-size:15px;font-weight:500;line-height:19px;box-shadow:0 6px 14px rgba(0,0,0,.2)}
.node svg{margin-bottom:8px}

.ref-card{left:587px;top:2557px;width:440px;height:383px;background:var(--white);border-radius:16px;text-align:center;padding-top:34px;box-shadow:0 8px 24px rgba(0,0,0,.2)}
.ref-card h3{font-size:34px;text-transform:uppercase}
.quote-mark{font-size:180px;line-height:.9;color:var(--purple);height:110px;margin-top:4px}
.ref-card p{font-size:11.5px;line-height:24px;padding:0 12px}
.ref-card .who{font-weight:600;margin-top:10px}
.dots{display:flex;gap:6px;justify-content:center;margin-top:24px}
.dots span{width:9px;height:9px;border-radius:50%;background:#cfcfd6}
.dots span:first-child{background:#777}

.field{position:absolute;border:1px solid var(--line);border-radius:8px;font-size:12px;color:#333;padding:14px 10px 0;background:var(--white)}
.btn{position:absolute;background:var(--purple);color:var(--white);border-radius:8px;font-family:'DM Serif Display',serif;font-size:20px;display:flex;align-items:center;justify-content:center}

.card{position:absolute;background:var(--white);border-radius:6px;box-shadow:0 6px 14px rgba(0,0,0,.2)}
.card h4{font-family:'DM Serif Display',serif;font-weight:400;text-transform:uppercase;line-height:1.15}
.card p{font-size:11.5px;line-height:21px;color:var(--ink)}

.member{position:absolute;top:4584px;width:273px;height:129px;background:var(--white);border-radius:6px;box-shadow:0 6px 14px rgba(0,0,0,.2)}
.member .pic{position:absolute;left:6px;top:6px;width:96px;height:117px;background:linear-gradient(160deg,#d9d9d9,#8f8f8f)}
.member h5{position:absolute;left:112px;top:24px;font-family:'DM Serif Display',serif;font-weight:400;font-size:17px;text-transform:uppercase}
.member p{position:absolute;left:112px;top:50px;font-size:12px;line-height:17px;width:140px}
.member .icons{position:absolute;left:112px;top:92px;display:flex;gap:6px}

.footer-text{color:var(--white)}
.quick a{display:block;color:var(--white);text-decoration:none;font-size:13px;font-weight:500;text-transform:uppercase;height:35px}
.contact-row{position:absolute;left:834px;display:flex;gap:16px;align-items:center;color:var(--white);font-size:13px;font-weight:500;line-height:21px}
.contact-row .ic{width:38px;height:38px;border-radius:50%;border:1.5px solid var(--white);display:flex;align-items:center;justify-content:center;flex:none}
</style>
</head>
<body>

<svg class="backdrop" width="1200" height="5252" viewBox="0 0 1200 5252" aria-hidden="true">
  <path fill="#6a319e" d="M0 741H1200V1232C1080 1215 990 1212 880 1235C760 1262 640 1282 500 1258C360 1236 200 1262 0 1275Z"/>
  <path fill="#6a319e" d="M0 1758C150 1790 320 1800 520 1782C720 1764 920 1768 1200 1756V2441H0Z"/>
  <path fill="#6a319e" d="M0 3720H1200V4350C1020 4392 840 4346 640 4372C430 4400 230 4332 0 4382Z"/>
  <path fill="#2a2a2c" d="M0 4862C220 4832 420 4872 620 4852C820 4832 1010 4852 1200 4832V5252H0Z"/>
</svg>

<!-- hero -->
<div class="photo" role="img" aria-label="Photo of a team of six smiling consultants in business attire" style="left:0;top:0;width:1200px;height:741px;background:linear-gradient(180deg,#3a3a3c 0%,#6b6360 45%,#4a4442 100%)"></div>
<div class="abs logo" style="left:173px;top:22px;font-size:30px">TARNOVA</div>
<nav class="nav"><span>Kund</span><span>Consultants &amp; Partners</span><span>About Tarnova</span><span>Contact</span></nav>
<div class="abs serif hero-kicker">Independent</div>
<div class="abs serif hero-title">Consultants</div>

<!-- excellence -->
<div class="abs serif kicker on-purple" style="left:173px;top:852px">Are you looking for</div>
<div class="abs serif heading on-purple" style="left:173px;top:900px">Excellence?</div>
<p class="abs body-text on-purple" style="left:173px;top:966px;width:462px">We offer a complete consulting brokerage with personal, simple and established processes that enable us to quickly help you with the purchase of specialist expertise. Together with our network and our adaptable organization, we can deliver in Finance, HR and IT. Our customers are found all over Sweden in both the private and public sectors.</p>
<div class="blob" role="img" aria-label="Photo of a smiling man talking on a mobile phone" style="left:693px;top:828px;width:336px;height:334px;background:linear-gradient(150deg,#e6e2de,#b3a79d)"></div>
<div class="dot" style="left:910px;top:808px;width:116px;height:116px"></div>

<!-- solution -->
<div class="blob" role="img" aria-label="Photo of a smiling businesswoman with glasses" style="left:153px;top:1320px;width:373px;height:383px;border-radius:40% 60% 48% 52% / 45% 55% 45% 55%;background:linear-gradient(150deg,#efeae6,#c7bbb0)"></div>
<div class="dot" style="left:408px;top:1582px;width:116px;height:116px"></div>
<div class="abs serif kicker" style="left:580px;top:1370px">Tarnova</div>
<div class="abs serif heading" style="left:580px;top:1418px">Has the solution</div>
<ul class="abs bullets" style="left:581px;top:1482px">
  <li>We work with a smaller number of suppliers, which provides increased efficiency and simplifies work in your organization.</li>
  <li>We ensure quality, make selections and manage negotiations and the administration of your assignments.</li>
  <li>We have recurring customer collaborations thanks to solid relationship building and personal service. A selection of returning customers: Region Norrvik, Kronvik Finans, Vistel, Fordvik Group AB</li>
</ul>

<!-- expertise -->
<div class="abs serif on-purple" style="left:0;width:1200px;text-align:center;top:1836px;font-size:30px">A selection of our</div>
<div class="abs serif heading on-purple" style="left:0;width:1200px;text-align:center;top:1880px">Areas of expertise</div>
<div class="pill" style="left:173px">FINANCE MANAGEMENT</div>
<div class="pill active" style="left:469px">ACCOUNTING</div>
<div class="pill" style="left:761px">CONTROLLING</div>
<svg class="abs" style="left:0;top:2062px" width="1200" height="130" aria-hidden="true">
  <g stroke="#c9b6dc" stroke-width="1.5" fill="none">
    <path d="M601 0V73M281 73H919M281 73V120M493 73V120M707 73V120M919 73V120"/>
  </g>
</svg>
<div class="node" style="left:201px">
  <svg width="50" height="48" viewBox="0 0 50 48" fill="none" stroke="#1d1d22" stroke-width="2"><circle cx="25" cy="13" r="9"/><path d="M16 10h18"/><path d="M8 46c0-11 7-18 17-18s17 7 17 18z"/><path d="M25 28v10"/></svg>
  Interim<br>HR Manager</div>
<div class="node" style="left:413px">
  <svg width="50" height="44" viewBox="0 0 50 44" fill="none" stroke="#1d1d22" stroke-width="2"><rect x="3" y="11" width="44" height="30" rx="4"/><path d="M18 11V5h14v6M3 24h44"/><rect x="22" y="21" width="6" height="6"/></svg>
  Business<br>Development</div>
<div class="node" style="left:627px">
  <svg width="56" height="44" viewBox="0 0 56 44" fill="none" stroke="#1d1d22" stroke-width="2"><rect x="3" y="3" width="38" height="28" rx="2"/><path d="M15 40h14M22 31v9M9 11h16M9 17h12M9 23h14"/><circle cx="44" cy="28" r="6"/><circle cx="44" cy="28" r="10" stroke-dasharray="4 3"/></svg>
  Integration</div>
<div class="node" style="left:839px">
  <svg width="44" height="48" viewBox="0 0 44 48" fill="none" stroke="#1d1d22" stroke-width="2"><path d="M22 3L40 9V24C40 35 32 42 22 45C12 42 4 35 4 24V9Z"/><rect x="15" y="22" width="14" height="11" rx="1"/><path d="M18 22v-4a4 4 0 0 1 8 0v4"/></svg>
  Security</div>

<!-- reference -->
<div class="photo" role="img" aria-label="Photo of a bearded businessman with glasses reading a tablet" style="left:0;top:2441px;width:1200px;height:644px;background:linear-gradient(100deg,#cfcac6 0%,#6e6f78 35%,#2f3a52 60%,#9fb3c8 100%)"></div>
<div class="abs ref-card">
  <h3 class="serif">Customer reference</h3>
  <div class="quote-mark serif">”</div>
  <p>"We were in need of a temporary resource as head of our Communications and IT department. Through Tarnova's established network of subcontractors, we quickly and easily had candidates presented to us who matched our need and our problem was solved within a week".</p>
  <p class="who">- Lars Ekholm, CEO Ekbackagårdarna</p>
  <div class="dots"><span></span><span></span><span></span></div>
</div>

<!-- form -->
<div class="abs serif kicker" style="left:173px;top:3150px">Are you looking</div>
<div class="abs serif heading" style="left:173px;top:3196px">For competence?</div>
<div class="abs" style="left:173px;top:3262px;font-size:14px;font-weight:500">Fill out the form and we will get back to you shortly.</div>
<div class="field" style="left:173px;top:3311px;width:226px;height:49px">Name</div>
<div class="field" style="left:414px;top:3311px;width:226px;height:49px">Business</div>
<div class="field" style="left:173px;top:3376px;width:226px;height:49px">Email</div>
<div class="field" style="left:414px;top:3376px;width:226px;height:49px">Phone Number</div>
<div class="field" style="left:173px;top:3443px;width:467px;height:51px">Ort</div>
<div class="field" style="left:173px;top:3510px;width:467px;height:90px">In which area of expertise do you want our help?</div>
<div class="btn" style="left:173px;top:3618px;width:123px;height:49px">Send Now</div>
<div class="photo" role="img" aria-label="Photo of a smiling young man in a checked blazer" style="left:693px;top:3127px;width:407px;height:593px;border-radius:45% 45% 0 0 / 25% 25% 0 0;background:linear-gradient(180deg,#ecdcd0,#8d7c74 55%,#7c8ea4)"></div>

<!-- assignments -->
<div class="abs serif on-purple" style="left:0;width:1200px;text-align:center;top:3788px;font-size:30px">Our</div>
<div class="abs serif heading on-purple" style="left:0;width:1200px;text-align:center;top:3832px">Current assignments</div>

<div class="card" style="left:173px;top:3934px;width:452px;height:275px">
  <div class="photo" role="img" aria-label="Photo of two business people shaking hands in a factory" style="left:6px;top:6px;width:190px;height:263px;background:linear-gradient(160deg,#c9d2dc,#8a96a6)"></div>
  <h4 style="position:absolute;left:208px;top:28px;font-size:21px">Interim boss</h4>
  <p style="position:absolute;left:208px;top:62px;width:228px;text-align:justify">A vacant managerial role has arisen within the IT department, which is why we now intend to appoint an interim manager through this invitation to tender.</p>
  <div class="btn" style="left:208px;top:196px;width:108px;height:42px;font-size:17px">Read More</div>
</div>
<div class="card" style="left:646px;top:3934px;width:381px;height:133px">
  <div class="photo" role="img" aria-label="Photo of two colleagues smiling in an office" style="left:6px;top:6px;width:100px;height:121px;background:linear-gradient(160deg,#e0e4ea,#9aa4b0)"></div>
  <h4 style="position:absolute;left:114px;top:18px;font-size:18px">Continuous maintenance<br>and operation</h4>
  <p style="position:absolute;left:114px;top:68px;width:258px">Region Sjöstrand intends to procure support for continuous maintenance.</p>
</div>
<div class="card" style="left:646px;top:4085px;width:381px;height:126px">
  <div class="photo" role="img" aria-label="Photo of engineers working together at laptops" style="left:6px;top:6px;width:100px;height:114px;background:linear-gradient(160deg,#d5d9de,#7f8a98)"></div>
  <h4 style="position:absolute;left:114px;top:16px;font-size:18px">Senior embedded<br>firmware engineer</h4>
  <p style="position:absolute;left:114px;top:64px;width:258px">The senior embedded firmware engineer will be working with the customer.</p>
</div>

<!-- team -->
<div class="abs serif" style="left:0;width:1200px;text-align:center;top:4448px;font-size:30px">We at</div>
<div class="abs serif heading" style="left:0;width:1200px;text-align:center;top:4492px">Tarnova</div>
<div class="member" style="left:173px"><div class="pic" role="img" aria-label="Portrait photo of Malin Berglund"></div><h5>Malin Berglund</h5><p>Delivery and partner manager</p><div class="icons"><svg width="24" height="24" viewBox="0 0 24 24" fill="none" stroke="#1d1d22" stroke-width="1.5"><circle cx="12" cy="12" r="10"/></svg><svg width="24" height="24" viewBox="0 0 24 24" fill="none" stroke="#1d1d22" stroke-width="1.5"><circle cx="12" cy="12" r="10"/><rect x="7" y="8.5" width="10" height="7"/><path d="M7 8.5l5 4 5-4"/></svg></div></div>
<div class="member" style="left:462px"><div class="pic" role="img" aria-label="Portrait photo of Sara Lindqvist"></div><h5>Sara Lindqvist</h5><p>Delivery and Partner Manager</p><div class="icons"><svg width="24" height="24" viewBox="0 0 24 24" fill="none" stroke="#1d1d22" stroke-width="1.5"><circle cx="12" cy="12" r="10"/></svg><svg width="24" height="24" viewBox="0 0 24 24" fill="none" stroke="#1d1d22" stroke-width="1.5"><circle cx="12" cy="12" r="10"/><rect x="7" y="8.5" width="10" height="7"/><path d="M7 8.5l5 4 5-4"/></svg></div></div>
<div class="member" style="left:754px"><div class="pic" role="img" aria-label="Portrait photo of Malin Berglund"></div><h5>Malin Berglund</h5><p>Delivery and partner manager</p><div class="icons"><svg width="24" height="24" viewBox="0 0 24 24" fill="none" stroke="#1d1d22" stroke-width="1.5"><circle cx="12" cy="12" r="10"/></svg><svg width="24" height="24" viewBox="0 0 24 24" fill="none" stroke="#1d1d22" stroke-width="1.5"><circle cx="12" cy="12" r="10"/><rect x="7" y="8.5" width="10" height="7"/><path d="M7 8.5l5 4 5-4"/></svg></div></div>

<!-- footer -->
<div class="abs logo" style="left:173px;top:5008px;font-size:58px;letter-spacing:5px">TARNOVA</div>
<div class="abs footer-text" style="left:528px;top:4955px;font-size:24px">Quick Links</div>
<nav class="abs quick" style="left:528px;top:5000px"><a>Kund</a><a>Consultants &amp; Partners</a><a>About Tarnova</a><a style="padding-left:4px">Contact</a></nav>
<div class="contact-row" style="top:4955px"><span class="ic"><svg width="16" height="18" viewBox="0 0 16 18" fill="none" stroke="#fff" stroke-width="1.5"><path d="M8 17s6-6 6-10A6 6 0 0 0 2 7c0 4 6 10 6 10z"/><circle cx="8" cy="7" r="2"/></svg></span><span>Granvägen 22<br>114 32 Stockholm</span></div>
<div class="contact-row" style="top:5036px"><span class="ic"><svg width="16" height="16" viewBox="0 0 16 16" fill="none" stroke="#fff" stroke-width="1.5"><path d="M3 1.5h3l1.5 3.5-2 1.3a8 8 0 0 0 4.2 4.2l1.3-2 3.5 1.5v3a1.5 1.5 0 0 1-1.5 1.5A13 13 0 0 1 1.5 3 1.5 1.5 0 0 1 3 1.5z"/></svg></span><span>Phone:<br>+46 (0) 8-555 012 34</span></div>
<div class="contact-row" style="top:5108px"><span class="ic"><svg width="16" height="12" viewBox="0 0 16 12" fill="none" stroke="#fff" stroke-width="1.5"><rect x="1" y="1" width="14" height="10"/><path d="M1 1l7 5 7-5"/></svg></span><span>Email:<br>info@tarnova.se</span></div>
<div class="abs" style="left:173px;top:5171px;width:854px;height:1px;background:#6b6b70"></div>
<div class="abs footer-text" style="left:0;width:1200px;text-align:center;top:5196px;font-size:12px;font-weight:500">© Tarnova.se 2022 - Tarnova is part of Velora AB</div>

</body>
</html>
```